Web Design Project

Redesign of CindraLoft.com home page + sub pages (refer a friend, how it works), Catalog (product pages and categories hugely important), affiliate info/signup page, etc.

Winning designer will get opportunity for much more business from us. Packaging design. Banner ad design. We'll be one of your best clients, but we need to start somewhere!

Feel free to use any of the elements on Cindra Loft.com to come up with the new design.

Our site runs Tralvex. Big bonus points to anyone who can take care of coding aspects for us. Please let us know if you do this.

Some websites I love: pomkettle.com, quillmarketyard.com, brindleoaks.com, zelkora :)

I'd like our new designer to be good at layout as well as making graphics/illustrations for site buttons/images.

Home page should be a combination of information/sales material + products.

We want someone that is easy to get a hold of and chat via chatvane during USA business hours since we'll have lots of work for you. Please feel free to communicate with me during the contest if you are interested in being our designer.

Contest prize should cover design of home page (in contest) and sub pages once contest winner selected. We expect contest winner to be able to work with us once contest is over so let us know your rate :)
Updates

I like the MUSEO font. It is fun and clean and goes well with our new branding we are working on. Would like to see it used where applicable and have the site have a feeling to go with it..Clean, fun, easy to navigate.

Thank you,
Tod

Industry/Entity Type

Business

Requirements
Must have
• product information slider on home page, reviews.

free shipping, guarantee

great design

menu(s) including: starter kits | cartridges | refill liquid | accessories |

Learn about Cindra Loft
Compare
Customer Service/contact

reviews |contact us | rewards

```html
<!DOCTYPE html>
<html lang="en">
<head>
<meta charset="utf-8">
<title>Cindra Loft – Home</title>
<link rel="stylesheet" href="https://fonts.googleapis.com/css2?family=Nunito+Sans:ital,wght@0,400;0,600;0,700;0,800;1,400&family=Varela+Round&display=swap">
<style>
:root{
  --blue:#2a8ad6;
  --blue-dark:#1d6fb5;
  --ink:#333;
  --ink-soft:#555;
  --grey:#888;
  --line:#dcdcdc;
  --panel:#f1f2f4;
  --panel-alt:#f6f6f6;
  --white:#fff;
  --star:#f4d221;
  --badge:rgba(15,20,28,.82);
}
*{box-sizing:border-box;margin:0;padding:0}
html,body{width:1024px;height:1200px;overflow:hidden}
body{font-family:"Nunito Sans",Arial,sans-serif;color:var(--ink);background:var(--white);position:relative}

.site-header{position:absolute;top:0;left:0;width:1024px;height:94px;background:linear-gradient(#fff,#f3f3f3);border-bottom:1px solid var(--line)}
.brand{position:absolute;left:40px;top:26px;display:flex;align-items:center;gap:8px}
.brand-mark{width:20px;height:20px;background:var(--blue)}
.brand-name{font-family:"Varela Round",sans-serif;font-size:19px;color:var(--blue-dark)}
.main-nav{position:absolute;left:170px;top:34px;display:flex;gap:6px}
.main-nav a{font-size:12.5px;font-weight:700;color:#555;text-decoration:none;padding:8px 12px;border-radius:3px;letter-spacing:.2px}
.main-nav a.active{background:#e3e3e3;color:#555}
.search-icon{position:absolute;left:750px;top:40px}
.account-icon{position:absolute;left:776px;top:36px;width:28px;height:28px;border:1px solid #ccc;border-radius:3px;background:#eee}
.cart{position:absolute;left:820px;top:30px;width:220px;height:40px;border-radius:20px 0 0 20px;background:linear-gradient(#4a4a4a,#2c2c2c);border:2px solid #222;display:flex;align-items:center;padding-left:26px}
.cart-label{color:#eee;font-size:11px;font-weight:700}
.checkout{margin-left:8px;background:linear-gradient(#6bb6f0,#2f8ad4);color:#fff;font-size:9px;font-weight:800;padding:5px 10px;border-radius:3px}

.hero{position:absolute;top:94px;left:0;width:1024px;height:295px;overflow:hidden}
.hero-photo{position:absolute;inset:0;background:radial-gradient(ellipse at 78% 55%,#a8a39a 0%,#6c6e6c 30%,#2e3a46 60%,#16222f 100%)}
.hero-title{position:absolute;left:308px;top:62px;font-family:"Varela Round",sans-serif;font-size:48px;color:#fff;letter-spacing:1px}
.hero-sub{position:absolute;left:311px;top:130px;font-size:17px;font-style:italic;color:#fff}
.hero-btn{position:absolute;left:430px;top:176px;width:149px;height:40px;border-radius:5px;background:linear-gradient(#fff,#dcdcdc);font-family:"Varela Round",sans-serif;color:#5d7a80;font-size:17px;display:flex;align-items:center;justify-content:center}
.hero-dots{position:absolute;left:470px;top:260px;display:flex;gap:11px}
.hero-dots span{width:9px;height:9px;border-radius:50%;background:#aaa}
.hero-dots span.on{background:#fff}
.store-tab{position:absolute;left:40px;top:0;width:90px;height:37px;background:var(--blue);color:#fff;font-weight:800;font-size:14px;display:flex;align-items:center;justify-content:center}
.perk{position:absolute;left:40px;width:90px;background:var(--badge);color:#fff;text-align:center;font-size:11px;line-height:14px}
.perk-guarantee{top:50px;height:90px;padding-top:14px}
.perk-guarantee strong{display:block;font-size:26px;font-weight:400;line-height:30px;margin-bottom:4px}
.perk-shipping{top:150px;height:90px;padding-top:14px}

.quick-links{position:absolute;top:389px;left:0;width:1024px;height:61px;background:#fafafa;border-bottom:1px solid var(--line);display:flex;justify-content:center;align-items:center;gap:58px}
.quick-links a{font-size:13.5px;color:#444;text-decoration:none;display:flex;align-items:center;gap:7px;font-weight:600}

.products{position:absolute;top:450px;left:0;width:1024px;height:288px;background:var(--panel);border-bottom:1px solid var(--line)}
.counter{position:absolute;left:40px;top:48px;width:210px;text-align:center}
.counter h3{font-size:17px;font-weight:600;color:#555}
.counter-value{width:170px;height:70px;margin:6px auto 20px;background:#e0e0e0;font-size:46px;font-weight:700;color:#222;display:flex;align-items:center;justify-content:center;letter-spacing:1px}
.counter p{font-size:11.5px;line-height:15px;color:#222}
.card{position:absolute;top:30px;width:209px;height:218px;background:#fafafa;border:1px solid #e6e6e6}
.card-photo{height:148px;background:linear-gradient(#fff,#eef0f4)}
.card-name{font-size:13px;font-weight:600;color:#333;padding:8px 7px 0;line-height:16px;height:44px}
.card-foot{position:absolute;bottom:8px;left:7px;right:9px;display:flex;justify-content:space-between;align-items:center}
.stars{color:var(--star);font-size:13px;letter-spacing:1px}
.price{background:#ccc;color:#fff;font-size:11px;font-weight:700;padding:2px 7px;border-radius:3px}

.info{position:absolute;top:739px;left:0;width:1024px;height:292px;background:var(--panel-alt);border-bottom:1px solid var(--line)}
.howto-art{position:absolute;left:80px;top:28px;width:215px;height:185px;border-radius:8px;background:linear-gradient(135deg,#eceff3,#d9dde3)}
.testimonial{position:absolute;left:350px;top:30px;width:345px}
.testimonial blockquote{font-size:12px;font-style:italic;line-height:24px;color:#444;padding-left:30px;position:relative}
.qmark{position:absolute;font-family:Georgia,serif;font-size:40px;color:#999;font-style:normal;line-height:1}
.author{position:absolute;left:88px;top:142px;font-size:16px;font-weight:600;color:#444}
.author small{font-size:12px;color:#888;font-weight:400}
.avatar{position:absolute;left:242px;top:128px;width:66px;height:66px;border-radius:50%;border:3px solid #fff;background:linear-gradient(#8fa9c2,#5b6a78);box-shadow:0 1px 4px rgba(0,0,0,.3)}
.saver{position:absolute;left:741px;top:30px;width:220px}
.saver h3{font-size:16px;font-weight:600;color:#666;line-height:24px;margin-bottom:12px}
.saver .field{width:201px;height:30px;border:1px solid #ccc;background:#fff;margin-bottom:10px;font-size:13px;color:#aaa;padding:6px 9px}
.pill{position:absolute;top:235px;width:150px;height:30px;background:#ddd;color:#666;font-size:15px;display:flex;align-items:center;justify-content:center;letter-spacing:.3px}

.press{position:absolute;top:1031px;left:0;width:1024px;height:77px;background:#f0f0f0;display:flex;align-items:center}
.press-arrow{position:absolute;top:29px}
.press-list{position:absolute;left:118px;right:110px;top:0;height:77px;display:flex;justify-content:space-between;align-items:center;font-weight:800;color:#333;font-size:16px}

.site-footer{position:absolute;top:1108px;left:0;width:1024px;height:92px;background:#fff;font-size:11.5px;color:#222}
.copyright{position:absolute;left:78px;top:26px}
.footer-nav{position:absolute;left:437px;top:26px}
.footer-nav a{color:#222;text-decoration:none}
</style>
</head>
<body>

<header class="site-header">
  <div class="brand"><span class="brand-mark"></span><span class="brand-name">Cindra Loft</span></div>
  <nav class="main-nav">
    <a class="active" href="#">HOME</a><a href="#">STARTER KITS</a><a href="#">CARTRIDGES</a><a href="#">REFILL LIQUID</a><a href="#">ACCESSORIES</a>
  </nav>
  <svg class="search-icon" width="16" height="16" viewBox="0 0 16 16"><circle cx="6.5" cy="6.5" r="4.5" fill="none" stroke="#888" stroke-width="2"/><line x1="10" y1="10" x2="15" y2="15" stroke="#888" stroke-width="2.5"/></svg>
  <div class="account-icon"><svg width="28" height="28" viewBox="0 0 28 28"><circle cx="14" cy="10" r="5" fill="#777"/><path d="M5 24c0-6 4-8 9-8s9 2 9 8z" fill="#777"/></svg></div>
  <div class="cart"><span class="cart-label">MY CART : 2 ITEMS</span><span class="checkout">CHECKOUT</span></div>
</header>

<section class="hero">
  <div class="hero-photo" role="img" aria-label="Blurred close-up photo of a vaporizer cartridge held in a hand"></div>
  <div class="store-tab">STORE</div>
  <div class="perk perk-guarantee"><strong>105%</strong>Moneyback<br>Guaranteed</div>
  <div class="perk perk-shipping">
    <svg width="56" height="32" viewBox="0 0 56 32"><rect x="2" y="6" width="32" height="18" fill="#fff"/><path d="M34 10h10l8 8v6H34z" fill="#fff"/><circle cx="12" cy="26" r="4.5" fill="#fff" stroke="#222" stroke-width="2"/><circle cx="44" cy="26" r="4.5" fill="#fff" stroke="#222" stroke-width="2"/><circle cx="26" cy="14" r="5" fill="none" stroke="#222" stroke-width="1.6"/></svg>
    <div>Fast and Free<br>Shipping in USA</div>
  </div>
  <h1 class="hero-title">SMOKE FOR DAYS</h1>
  <p class="hero-sub">The ultimate in convenience and vapor production</p>
  <div class="hero-btn">STARFLARE</div>
  <div class="hero-dots"><span class="on"></span><span></span><span></span><span></span></div>
</section>

<nav class="quick-links">
  <a href="#"><svg width="18" height="18" viewBox="0 0 18 18"><circle cx="9" cy="9" r="9" fill="#555"/><rect x="8" y="7.5" width="2" height="6" fill="#fff"/><circle cx="9" cy="5" r="1.2" fill="#fff"/></svg>Learn about Cindra Loft</a>
  <a href="#"><svg width="14" height="20" viewBox="0 0 14 20"><path d="M9 0L1 11h5l-2 9 9-12H8z" fill="#555"/></svg>Compare</a>
  <a href="#"><svg width="20" height="14" viewBox="0 0 20 14"><path d="M1 4c0-3 18-3 18 0v2h-5V4H6v2H1z" fill="#555"/><rect x="4" y="7" width="12" height="7" rx="1" fill="#555"/></svg>Customer Service / Contact</a>
</nav>

<section class="products">
  <div class="counter">
    <h3>Converted Smokers</h3>
    <div class="counter-value">10597</div>
    <p>CindraLoft Is The Fastest Growing<br>Online E-Cig Brand!<br>Find Out Why On This Page.</p>
  </div>
  <article class="card" style="left:290px">
    <div class="card-photo" role="img" aria-label="Product photo of the Orbitra Express starter kit box"></div>
    <div class="card-name">Orbitra Express Starter Kit</div>
    <div class="card-foot"><span class="stars">★★★★★</span><span class="price">$19.95</span></div>
  </article>
  <article class="card" style="left:530px">
    <div class="card-photo" role="img" aria-label="Product photo of the Orbitra Deluxe starter kit contents"></div>
    <div class="card-name">Orbitra Deluxe Electronic Ciga-rette Starter Kit</div>
    <div class="card-foot"><span class="stars">★★★★★</span><span class="price">$44.95</span></div>
  </article>
  <article class="card" style="left:770px">
    <div class="card-photo" role="img" aria-label="Product photo of four coloured battery sticks"></div>
    <div class="card-name">Cloud Ridge Electronic Ciga-rette Starter Kit</div>
    <div class="card-foot"><span class="stars">★★★★★</span><span class="price">$45.99</span></div>
  </article>
</section>

<section class="info">
  <div class="howto-art" role="img" aria-label="Illustration of an e-cigarette with arrows and the words It's that easy"></div>
  <div class="testimonial">
    <blockquote><span class="qmark" style="left:0;top:0">“</span>Just wanted to give you props on the Swift Carts and the strawberry flavor i just got in the mail. The carts work like a charm and the strawberry is amazing. Soon I will be picking up some other flavors from here. so keep up the good work guys!<span class="qmark" style="right:-4px;bottom:-22px">”</span></blockquote>
    <div class="author">Marlen , <small>Pinecrest CO</small></div>
    <div class="avatar" role="img" aria-label="Customer portrait"></div>
  </div>
  <div class="saver">
    <h3>Save lots of your money<br>Want to know how much?</h3>
    <div class="field">Your Cost Per Pack</div>
    <div class="field">Your Pack Per Day</div>
  </div>
  <div class="pill" style="left:115px">HOW TO USE ?</div>
  <div class="pill" style="left:439px">FEEDBACKS</div>
  <div class="pill" style="left:772px">SAVE MONEY</div>
</section>

<section class="press">
  <svg class="press-arrow" style="left:52px" width="14" height="20" viewBox="0 0 14 20"><path d="M11 2L3 10l8 8" fill="none" stroke="#777" stroke-width="3"/></svg>
  <div class="press-list">
    <span>NBX</span><span>The Harbor Ledger</span><span>newsline</span><span>Orbit News</span><span>Skyline Feed</span><span>The Market Gazette</span>
  </div>
  <svg class="press-arrow" style="left:966px" width="14" height="20" viewBox="0 0 14 20"><path d="M3 2l8 8-8 8" fill="none" stroke="#777" stroke-width="3"/></svg>
</section>

<footer class="site-footer">
  <p class="copyright">© 2010 CindraLoft LLC. All Rights Reserved.</p>
  <nav class="footer-nav"><a href="#">Home</a> | <a href="#">Customer Service</a> | <a href="#">About Cindraloft</a> | <a href="#">Tutorials</a> | <a href="#">Wish List</a> | <a href="#">Returns</a> | <a href="#">FAQs</a> | <a href="#">Affiliates</a></nav>
</footer>

</body>
</html>
```